International Clinical Software Company needs a new business card design

We are looking for a new business card design for our company that has recently expanded into the UK market, making us a multinational company.
After having rebranded our website and produced a new style guide, we are looking for a business card that is creative and attention grabbing, while being consistent with the style and colour scheme used on the new website, www.brookvale.example
We produce care management technology for the aged care market, but the main aspect we aim to communicate is the human element of our software, and the way it assists in providing better care for aged people, and stronger relationships between aged people and the staff that care for them.
Our current business card is a dark green with gold text, which makes the text quite difficult to read, not very aesthetically appealing and the colour scheme looks quite dated.
We would like something fresh and modern, that can still be colourful but doesn't use large blocks of dark colour, and uses the colours within our logo.
Something tying in with the leaves that are used in our logo could work quite nicely, along with the Autumn/Fall colours of soft greens, yellows and reds (also in our existing logo). However also happy to look at fresh, completely out of the box ideas we may not have yet considered.
Target Market(s)
The people that receive this business card work in the aged card or health industry and are either corporate/management level staff or clinical (Registered Nurses, care workers etc.)
Industry/Entity Type
Health Product
Contact Information for Business Card
Company Name - BrookvaleTech
Company locations: United Kingdom, Australia, New Zealand
Staff Details:
Staff name: Dermot Quill
Staff job title: Executive Chairman
Staff email: d.quill@brookvale.example
Office phone number: 01632 960418
Font styles to use
Other font styles liked:
- Calibri
Requirements
Must have
- Must include the BrookvaleTech brand name in it's current font
- Must include logo (3 leaves in gold circle)
- Must include Business Card Details
Nice to have
- Elements of gold
- White space
- Something autumn themed but not too cliched
Should not have
- No blue - used by a major competitor and we would like to differentiate from them
- Large blocks of dark green colour (the green that appears in our leaves on the logo on our current business card is the background colour and it is far too dark)

```html
<!DOCTYPE html>
<html lang="en">
<head>
<meta charset="utf-8">
<title>BrookvaleTech Business Card</title>
<link rel="stylesheet" href="https://fonts.googleapis.com/css2?family=Arimo:wght@400;700&display=swap">
<style>
  :root {
    --backdrop: #e6e4e0;
    --card-white: #ffffff;
    --gold: #b3a285;
    --gold-light: #cfc2a8;
    --gold-deep: #a08f72;
    --leaf-red: #c9553a;
    --leaf-orange: #e89a3a;
    --leaf-yellow: #e9d45a;
    --leaf-green: #9bb54a;
    --text-light: #ffffff;
    --brand: #b3a285;
  }
  * { box-sizing: border-box; margin: 0; padding: 0; }
  html, body {
    width: 1200px;
    height: 950px;
    overflow: hidden;
    background: var(--backdrop);
    font-family: "Arimo", Arial, sans-serif;
  }
  .business-card {
    position: absolute;
    left: 100px;
    top: 185px;
    width: 1000px;
    height: 580px;
    background: var(--card-white);
    overflow: hidden;
    box-shadow: 0 10px 30px rgba(0,0,0,0.15);
  }
  .card-artwork {
    position: absolute;
    inset: 0;
    width: 1000px;
    height: 580px;
  }
  .brand-lockup {
    position: absolute;
    left: 70px;
    top: 200px;
    display: flex;
    flex-direction: column;
    align-items: center;
    gap: 22px;
  }
  .brand-mark {
    width: 96px;
    height: 96px;
    border-radius: 50%;
    background: var(--gold);
  }
  .brand-name {
    font-size: 44px;
    font-weight: 400;
    color: var(--brand);
    letter-spacing: 0.5px;
  }
  .contact-block {
    position: absolute;
    right: 40px;
    top: 190px;
    text-align: right;
    color: var(--text-light);
  }
  .staff-name {
    font-size: 32px;
    font-weight: 700;
    margin-bottom: 6px;
  }
  .staff-title {
    font-size: 21px;
    margin-bottom: 22px;
  }
  .contact-line {
    display: flex;
    justify-content: flex-end;
    align-items: center;
    gap: 12px;
    font-size: 20px;
    line-height: 34px;
  }
  .contact-icon {
    width: 20px;
    height: 20px;
    flex: none;
  }
  .locations {
    font-size: 20px;
    margin-top: 14px;
  }
</style>
</head>
<body>
  <div class="business-card">
    <svg class="card-artwork" viewBox="0 0 1000 580" xmlns="http://www.w3.org/2000/svg">
      <defs>
        <linearGradient id="gold-field" x1="0" y1="0" x2="1" y2="1">
          <stop offset="0" stop-color="#d4c8b0"/>
          <stop offset="0.5" stop-color="#b3a285"/>
          <stop offset="1" stop-color="#a08f72"/>
        </linearGradient>
        <linearGradient id="leaf-tones" x1="1" y1="0" x2="0" y2="1">
          <stop offset="0" stop-color="#9bb54a"/>
          <stop offset="0.18" stop-color="#c9553a"/>
          <stop offset="0.4" stop-color="#e89a3a"/>
          <stop offset="0.6" stop-color="#e9d45a"/>
          <stop offset="0.8" stop-color="#e08a3c"/>
          <stop offset="1" stop-color="#c9553a"/>
        </linearGradient>
      </defs>
      <path class="gold-field" fill="url(#gold-field)"
            d="M1000 0 L1000 580 L0 580 L0 530 C200 520 330 470 420 360 C500 250 560 90 700 0 Z"/>
      <path class="leaf-cascade" role="img"
            aria-label="Illustration of autumn leaves in red, orange, yellow and green cascading from the top right corner down to the bottom left"
            fill="url(#leaf-tones)" opacity="0.92"
            d="M560 0 L920 0 C880 80 760 150 640 200 C560 320 520 440 400 520 C280 570 120 575 40 560 C140 520 260 490 340 420 C420 330 460 200 520 120 Z"/>
    </svg>

    <div class="brand-lockup">
      <div class="brand-mark"></div>
      <div class="brand-name">BrookvaleTech</div>
    </div>

    <div class="contact-block">
      <div class="staff-name">Dermot Quill</div>
      <div class="staff-title">Executive Chairman</div>
      <div class="contact-line">
        <span>01632 960418</span>
        <svg class="contact-icon" viewBox="0 0 24 24" aria-hidden="true">
          <path fill="#fff" d="M6.6 10.8c1.4 2.8 3.8 5.1 6.6 6.6l2.2-2.2c.3-.3.7-.4 1-.2 1.1.4 2.3.6 3.6.6.6 0 1 .4 1 1V20c0 .6-.4 1-1 1C10.6 21 3 13.4 3 4c0-.6.4-1 1-1h3.5c.6 0 1 .4 1 1 0 1.3.2 2.5.6 3.6.1.3 0 .7-.2 1z"/>
        </svg>
      </div>
      <div class="contact-line">
        <span>d.quill@brookvale.example</span>
        <svg class="contact-icon" viewBox="0 0 24 24" aria-hidden="true">
          <rect x="2" y="5" width="20" height="14" rx="1.5" fill="#fff"/>
          <path d="M3 6.5 L12 13 L21 6.5" fill="none" stroke="#b3a285" stroke-width="1.8"/>
        </svg>
      </div>
      <div class="contact-line">
        <span>www.brookvale.example</span>
        <svg class="contact-icon" viewBox="0 0 24 24" aria-hidden="true">
          <circle cx="12" cy="12" r="9.5" fill="#fff"/>
          <ellipse cx="12" cy="12" rx="4" ry="9.5" fill="none" stroke="#b3a285" stroke-width="1.5"/>
          <path d="M2.5 12 H21.5" stroke="#b3a285" stroke-width="1.5"/>
        </svg>
      </div>
      <div class="locations">United Kingdom, Australia, New Zealand</div>
    </div>
  </div>
</body>
</html>
```